Webdesign Birkental

Conversion of the site https://www.gasthaus-birkental.de/ The Deisgn should be modern and according to the latest stadtard SEO etc.

```html
<!DOCTYPE html>
<html lang="en">
<head>
<meta charset="utf-8">
<title>Gasthaus Birkental</title>
<link rel="stylesheet" href="https://fonts.googleapis.com/css2?family=Open+Sans:wght@400;600;700;800&display=swap">
<style>
:root{
  --red:#b5122b;
  --green:#4caf1a;
  --green-dark:#3b8f12;
  --ink:#333;
  --grey:#666;
  --footer:#252525;
  --footer-text:#cfcfcf;
}
*{box-sizing:border-box;margin:0;padding:0}
html,body{width:1200px;height:5328px;overflow:hidden;background:#fff;font-family:"Open Sans",Arial,sans-serif;color:var(--ink)}
.page{position:relative;width:1200px;height:5328px;overflow:hidden}
.abs{position:absolute}
.brand{font-weight:800;color:var(--red);text-transform:uppercase;letter-spacing:1px;line-height:1}
.brand small{display:block;text-transform:none;letter-spacing:0}
.site-header{left:0;top:0;width:1200px;height:140px;background:#fff}
.site-header .brand{left:84px;top:30px;font-size:44px;width:340px}
.site-header .brand small{font-size:22px;margin-bottom:4px}
.call{left:668px;top:26px;display:flex;align-items:center;gap:10px}
.call .ico{width:36px;height:36px;border-radius:50%;border:3px solid var(--red);display:flex;align-items:center;justify-content:center}
.call p{font-size:14px;line-height:1.2;color:var(--red);font-weight:700}
.call p span{display:block;color:var(--ink);font-weight:600}
.search{left:862px;top:28px;width:250px;height:34px;border:1px solid #ddd;border-radius:4px;display:flex;align-items:center;justify-content:space-between;padding:0 4px 0 10px;font-size:13px;color:#999}
.search b{width:26px;height:26px;border-radius:50%;background:var(--red);display:flex;align-items:center;justify-content:center}
.main-nav{left:418px;top:98px;display:flex;gap:30px;font-size:16px;font-weight:600}
.hero{left:0;top:140px;width:1200px;height:720px;background:
  radial-gradient(ellipse 420px 120px at 720px 460px,rgba(238,232,220,.9),rgba(238,232,220,0) 70%),
  radial-gradient(ellipse 300px 200px at 150px 380px,rgba(40,52,30,.85),rgba(40,52,30,0) 70%),
  radial-gradient(ellipse 200px 80px at 660px 560px,rgba(120,100,160,.7),rgba(120,100,160,0) 70%),
  radial-gradient(ellipse 160px 70px at 1080px 600px,rgba(170,30,40,.55),rgba(170,30,40,0) 70%),
  linear-gradient(180deg,#c7d0d6 0%,#d9d2c2 18%,#7d8a58 32%,#55623a 48%,#8a7f6c 62%,#6c6a64 78%,#4d4a45 100%)}
.hero-curve{left:0;top:780px;width:1200px;height:100px}
.scroll-cue{left:588px;top:840px;width:24px;height:38px;border:2px solid #888;border-radius:12px;background:#fff}
h2{font-size:40px;font-weight:700;text-transform:uppercase;text-align:center;color:var(--ink)}
h2 em{font-style:normal;color:var(--red)}
.about{left:150px;top:930px;width:900px;text-align:center}
.about p{font-size:15.5px;line-height:1.75;margin-top:22px}
.btn{display:inline-flex;align-items:center;gap:10px;background:var(--green);color:#fff;font-weight:700;font-size:16px;border-radius:30px;padding:12px 28px;border-bottom:3px solid var(--green-dark)}
.btn i{width:18px;height:18px;border-radius:50%;background:#fff;display:inline-flex;align-items:center;justify-content:center}
.restaurant-bg{left:0;top:1420px;width:1200px;height:720px;background:linear-gradient(180deg,#ecebe8,#f6f5f3 50%,#e9e7e4)}
.restaurant-text{left:160px;top:1596px;width:880px;text-align:center}
.restaurant-text h2{color:var(--red);font-size:36px}
.lead{font-size:15px;line-height:1.6;color:var(--grey);margin-top:14px}
.tile{width:330px;height:330px;border-radius:50%;border:7px solid var(--green);box-shadow:0 0 0 5px #fff;display:flex;align-items:center;justify-content:center;text-align:center;color:#fff;font-size:32px;font-weight:800;text-transform:uppercase;line-height:1.15;text-shadow:0 2px 6px rgba(0,0,0,.7)}
.t1{background:radial-gradient(circle at 50% 75%,#b9a88a,rgba(185,168,138,0) 45%),linear-gradient(180deg,#2f3e4c 0%,#4d6272 45%,#7f7663 75%,#3f3a33 100%)}
.t2{background:radial-gradient(circle at 35% 40%,#c9b59a,rgba(201,181,154,0) 40%),linear-gradient(160deg,#8a6a55,#4a2c26 60%,#7a1f26)}
.t3{background:radial-gradient(circle at 60% 35%,#d8b273,rgba(216,178,115,0) 35%),linear-gradient(160deg,#6a6064,#2f2a2e 60%,#5a3a2c)}
.gallery-text{left:140px;top:2236px;width:920px;text-align:center}
.ph{position:absolute}
.g1{background:radial-gradient(ellipse at 30% 70%,#a8402f,rgba(168,64,47,0) 55%),linear-gradient(180deg,#f1e6d3 0%,#d9b58f 45%,#8e5a42 100%)}
.g2{background:radial-gradient(ellipse at 75% 20%,#e6a24a,rgba(230,162,74,0) 40%),radial-gradient(ellipse at 50% 80%,#8d2f2c,rgba(141,47,44,0) 55%),linear-gradient(180deg,#f2ebe0 0%,#d7c4ad 50%,#6e4a3b 100%)}
.g3{background:radial-gradient(ellipse at 45% 60%,#f4f2ee,rgba(244,242,238,0) 35%),linear-gradient(180deg,#b7aea1 0%,#8a7a68 50%,#5d5044 100%)}
.g4{background:radial-gradient(ellipse at 50% 25%,#f7b47c,rgba(247,180,124,0) 60%),linear-gradient(180deg,#e98a5a 0%,#d9724a 50%,#7e4a38 100%)}
.g5{background:radial-gradient(ellipse at 50% 45%,#7ea23c,rgba(126,162,60,0) 35%),linear-gradient(180deg,#9b8f72 0%,#5c5a46 55%,#3a3a30 100%)}
.g6{background:linear-gradient(180deg,#c6d6e6 0%,#b9c7d1 40%,#b35a3a 52%,#86a85a 62%,#5f8a3a 100%)}
.g7{background:linear-gradient(180deg,#cfdbe7 0%,#a9c0d2 35%,#4d6a3a 55%,#78a34a 75%,#5e8b34 100%)}
.caterers-bg{left:0;top:3400px;width:1200px;height:580px;background:linear-gradient(90deg,#f1efec,#e6e3df 60%,#f4f3f1)}
.circle-photo{border-radius:50%;border:8px solid var(--green);box-shadow:0 0 0 5px #fff}
.caterers-photo{left:150px;top:3480px;width:340px;height:340px;background:radial-gradient(ellipse at 55% 45%,#e3e8f0,rgba(227,232,240,0) 30%),radial-gradient(ellipse at 40% 75%,#3d5d86,rgba(61,93,134,0) 45%),linear-gradient(150deg,#2b3847,#121922 55%,#6f7c86)}
.side-text h3{font-size:34px;font-weight:800;text-transform:uppercase;color:var(--red)}
.side-text h4{font-size:20px;font-weight:700;margin-top:8px}
.side-text p{font-size:15px;line-height:1.7;margin-top:16px}
.caterers-text{left:560px;top:3520px;width:540px}
.weddings-text{left:84px;top:4100px;width:520px}
.weddings-photo{left:680px;top:4040px;width:380px;height:380px;border-color:var(--red);background:radial-gradient(ellipse at 50% 55%,#6b3a1f,rgba(107,58,31,0) 40%),radial-gradient(ellipse at 30% 20%,#f6a94e,rgba(246,169,78,0) 45%),linear-gradient(180deg,#f0c48f,#b87242 55%,#efe3d3)}
.site-footer{left:0;top:4720px;width:1200px;height:608px;background:var(--footer)}
.footer-brand{left:0;width:1200px;top:4845px;text-align:center;font-size:48px}
.footer-brand small{font-size:26px;margin-bottom:6px}
.contact-item{width:300px;text-align:center;color:var(--footer-text);font-size:14px;line-height:1.5}
.contact-item .ring{width:70px;height:70px;border-radius:50%;background:var(--red);margin:0 auto 16px;display:flex;align-items:center;justify-content:center}
.footer-nav{left:0;width:1200px;top:5156px;display:flex;justify-content:center;gap:14px;color:var(--footer-text);font-size:13px}
.rule{left:250px;width:700px;top:5188px;height:1px;background:#555}
.copy{left:0;width:1200px;top:5200px;text-align:center;color:#999;font-size:12px}
.social{left:0;width:1200px;top:5252px;display:flex;justify-content:center;gap:10px}
.social span{width:24px;height:24px;border-radius:50%;border:1.5px solid #ccc}
</style>
</head>
<body>
<div class="page">

<header class="site-header abs">
  <div class="brand abs"><small>Gasthaus</small>Birkental</div>
  <div class="call abs">
    <span class="ico"><svg width="16" height="16" viewBox="0 0 24 24"><path fill="#b5122b" d="M6.6 10.8a15 15 0 0 0 6.6 6.6l2.2-2.2c.3-.3.7-.4 1-.2 1.1.4 2.3.6 3.6.6.6 0 1 .4 1 1V20c0 .6-.4 1-1 1A17 17 0 0 1 3 4c0-.6.4-1 1-1h3.5c.6 0 1 .4 1 1 0 1.3.2 2.5.6 3.6.1.3 0 .7-.2 1z"/></svg></span>
    <p>CALL US:<span>06321/5580</span></p>
  </div>
  <div class="search abs">Search<b><svg width="12" height="12" viewBox="0 0 24 24"><circle cx="10" cy="10" r="6" fill="none" stroke="#fff" stroke-width="3"/><path d="M15 15l6 6" stroke="#fff" stroke-width="3"/></svg></b></div>
  <nav class="main-nav abs"><span>About Us</span><span>Restaurant</span><span>Gallery</span><span>Events</span><span>Caterers</span><span>Weddings</span><span>Contact</span></nav>
</header>

<div class="hero abs" role="img" aria-label="Evening view of the lakeside guesthouse with trees, parasols and parked cars"></div>
<svg class="hero-curve abs" viewBox="0 0 1200 100" preserveAspectRatio="none"><path d="M0 20 Q600 110 1200 20 V100 H0Z" fill="#fff"/></svg>
<div class="scroll-cue abs"></div>

<section class="about abs">
  <h2>About <em>Gasthaus Birkental</em></h2>
  <p>Our guesthouse on the Birkental in Lindenau is an oasis of relaxation and recreation. Located directly on the Birkental we welcome our guests for a few hours "holiday". Also parking facilities are sufficiently available. The view from the open terrace with about 100 seats sweeps our popular beach bar, the playgrounds and recreational facilities for the "little" and "big" guests with tennis, basketball and soccer field right up to the lake in just a few steps can be reached.</p>
  <p>Very popular - especially on hot days - is our beach bar with music and cocktails. Every Thursday we "throw" on our grill, here is juicy steaks and grilled fish on the menu. Our restaurant with about 50 seats and newly designed children's play area spoils you with international and local cuisine.</p>
  <p style="margin-top:34px"><span class="btn">Read More <i><svg width="10" height="10" viewBox="0 0 10 10"><path d="M3 1l4 4-4 4" fill="none" stroke="#4caf1a" stroke-width="2"/></svg></i></span></p>
</section>

<div class="restaurant-bg abs"></div>
<svg class="abs" style="left:0;top:1400px" width="1200" height="120" viewBox="0 0 1200 120" preserveAspectRatio="none"><path d="M0 0 H1200 V20 Q600 130 0 30Z" fill="#fff"/><path d="M0 30 Q300 0 600 40 Q900 80 1200 60" fill="none" stroke="var(--red)" stroke-width="10"/></svg>
<section class="restaurant-text abs">
  <h2>Restaurant</h2>
  <p class="lead">Sed ut perspiciatis unde omnis iste natus error sit voluptatem accusantium doloremque laudantium, totam rem aperiam, eaque ipsa quae ab illo inventore veritatis et quasi architecto beatae vitae dicta sunt explicabo.</p>
</section>
<div class="tile t1 abs" style="left:85px;top:1730px" role="img" aria-label="Beach bar by the lake">Beach Bar</div>
<div class="tile t2 abs" style="left:435px;top:1730px" role="img" aria-label="Restaurant dining room">Restaurant<br>Menu</div>
<div class="tile t3 abs" style="left:785px;top:1730px" role="img" aria-label="Coach group dining">Menu for Bus<br>Travel</div>
<svg class="abs" style="left:0;top:2060px" width="1200" height="100" viewBox="0 0 1200 100" preserveAspectRatio="none"><path d="M0 20 Q600 90 1200 30 V100 H0Z" fill="#fff"/><path d="M0 40 Q600 110 1200 30" fill="none" stroke="var(--red)" stroke-width="10"/></svg>

<section class="gallery-text abs">
  <h2>Gallery of <em>Gasthaus Birkental</em></h2>
  <p class="lead">Sed ut perspiciatis unde omnis iste natus error sit voluptatem accusantium doloremque laudantium, totam rem aperiam, eaque ipsa quae ab illo inventore veritatis et quasi architecto beatae vitae dicta sunt explicabo.</p>
</section>
<div class="ph g1" style="left:75px;top:2400px;width:510px;height:275px" role="img" aria-label="Dining room set for guests"></div>
<div class="ph g2" style="left:605px;top:2400px;width:522px;height:520px" role="img" aria-label="Bright restaurant interior with laid tables"></div>
<div class="ph g3" style="left:75px;top:2695px;width:250px;height:365px" role="img" aria-label="Wedding couple dancing"></div>
<div class="ph g4" style="left:345px;top:2695px;width:240px;height:205px" role="img" aria-label="Terrace tables under parasols"></div>
<div class="ph g5" style="left:345px;top:2940px;width:240px;height:205px" role="img" aria-label="Host serving drinks at the bar"></div>
<div class="ph g6" style="left:605px;top:2940px;width:250px;height:205px" role="img" aria-label="Guesthouse seen across the lawn"></div>
<div class="ph g7" style="left:875px;top:2940px;width:252px;height:205px" role="img" aria-label="Play area on the meadow"></div>
<div class="abs" style="left:0;width:1200px;top:3195px;text-align:center"><span class="btn">View the entire gallery <i><svg width="10" height="10" viewBox="0 0 10 10"><path d="M3 1l4 4-4 4" fill="none" stroke="#4caf1a" stroke-width="2"/></svg></i></span></div>

<div class="caterers-bg abs"></div>
<svg class="abs" style="left:0;top:3380px" width="1200" height="100" viewBox="0 0 1200 100" preserveAspectRatio="none"><path d="M0 0 H1200 V70 Q600 -20 0 40Z" fill="#fff"/><path d="M0 40 Q600 -20 1200 70" fill="none" stroke="var(--red)" stroke-width="8"/></svg>
<div class="circle-photo caterers-photo abs" role="img" aria-label="Chefs at a catering buffet"></div>
<section class="side-text caterers-text abs">
  <h3>Caterers</h3>
  <h4>Your party service in Lindenau and surroundings!</h4>
  <p>Who wants to offer his guests delicious regional specialties, is in good hands at our party service! Whether cold plates or complete buffets are no problem for us: delicious fish specialties, cheese buffets, vegetarian dishes or Palatine delicacies - we cook and prepare in our kitchen and deliver everything fresh to your celebration.</p>
  <p style="margin-top:26px"><span class="btn">Read More <i><svg width="10" height="10" viewBox="0 0 10 10"><path d="M3 1l4 4-4 4" fill="none" stroke="#4caf1a" stroke-width="2"/></svg></i></span></p>
</section>
<svg class="abs" style="left:0;top:3920px" width="1200" height="100" viewBox="0 0 1200 100" preserveAspectRatio="none"><path d="M0 60 Q600 -10 1200 50 V100 H0Z" fill="#fff"/></svg>

<section class="side-text weddings-text abs">
  <h3>Weddings</h3>
  <h4>You want to get married?</h4>
  <p>We tailor your dream day to measure. All offers are put together individually for your wedding celebration. Our repertoire, on the terrace and the hall, ranges from elegant traditional to extravagant modern.</p>
  <p style="margin-top:22px"><span class="btn">Read More <i><svg width="10" height="10" viewBox="0 0 10 10"><path d="M3 1l4 4-4 4" fill="none" stroke="#4caf1a" stroke-width="2"/></svg></i></span></p>
</section>
<div class="circle-photo weddings-photo abs" role="img" aria-label="Chocolate fountain on the wedding buffet"></div>

<footer class="site-footer abs"></footer>
<svg class="abs" style="left:0;top:4690px" width="1200" height="80" viewBox="0 0 1200 80" preserveAspectRatio="none"><path d="M0 0 H1200 V10 Q600 90 0 10Z" fill="#fff"/><path d="M0 10 Q600 90 1200 10" fill="none" stroke="var(--red)" stroke-width="6"/></svg>
<div class="brand footer-brand abs"><small>Gasthaus</small>Birkental</div>
<div class="contact-item abs" style="left:160px;top:4990px"><div class="ring"><svg width="30" height="22" viewBox="0 0 30 22"><rect x="1" y="1" width="28" height="20" fill="none" stroke="#fff" stroke-width="2"/><path d="M1 1l14 11L29 1" fill="none" stroke="#fff" stroke-width="2"/></svg></div>Email<br>Info@Gasthaus-Birkental.de</div>
<div class="contact-item abs" style="left:450px;top:4990px"><div class="ring"><svg width="24" height="30" viewBox="0 0 24 30"><path d="M12 29S2 17 2 11a10 10 0 0 1 20 0c0 6-10 18-10 18z" fill="none" stroke="#fff" stroke-width="2"/><circle cx="12" cy="11" r="4" fill="#fff"/></svg></div>Am Seeweg 12, 67412<br>Lindenau</div>
<div class="contact-item abs" style="left:740px;top:4990px"><div class="ring"><svg width="26" height="26" viewBox="0 0 24 24"><path fill="#fff" d="M6.6 10.8a15 15 0 0 0 6.6 6.6l2.2-2.2c.3-.3.7-.4 1-.2 1.1.4 2.3.6 3.6.6.6 0 1 .4 1 1V20c0 .6-.4 1-1 1A17 17 0 0 1 3 4c0-.6.4-1 1-1h3.5c.6 0 1 .4 1 1 0 1.3.2 2.5.6 3.6.1.3 0 .7-.2 1z"/></svg></div>Phone:<br>06321/5580</div>
<nav class="footer-nav abs"><span>Home</span>|<span>About Us</span>|<span>Restaurant</span>|<span>Gallery</span>|<span>Events</span>|<span>Caterers</span>|<span>Weddings</span>|<span>Contact</span></nav>
<div class="rule abs"></div>
<p class="copy abs">© 2016 Company Name · All right reserved</p>
<div class="social abs"><span></span><span></span><span></span><span></span></div>

</div>
</body>
</html>
```